Website Design for a Law Firm

We require a fully functional Website that will be added features such as live chat, Online payment system and online forms. We need to be able to edit the website and update it regularly. We have made a website structure that is attached below.

The website footer must have:
Liability limited by a Scheme approved under Professional Standards Legislation. All legal practitioners employed by Brantley Lawyers Pty Limited (including those described as Principal Solicitor) are members of the Scheme.

Target Market(s)

People seeking legal services in Australia

Industry/Entity Type

Legal

Coding

Coded - Design and coding required

Number of Pages Required

1 page

Requirements
Must have
• Online portal function where clients can upload documents; website that would work perfectly on standard mobile, tablet, laptop, and desktop sizes; the website must have an online payment system.
Nice to have
• Online portal function where clients

```html
<!DOCTYPE html>
<html lang="en">
<head>
<meta charset="utf-8">
<title>Brantley Lawyers</title>
<link rel="stylesheet" href="https://fonts.googleapis.com/css2?family=Cinzel:wght@500;600;700&family=Libre+Baskerville:wght@400;700&family=Open+Sans:wght@400;600&display=swap">
<style>
:root{
  --green:#173a2c;
  --green-deep:#12301f;
  --gold:#c9a456;
  --gold-soft:#d2b06a;
  --mist:#dde2df;
  --ink:#1f2a24;
  --white:#ffffff;
}
*{box-sizing:border-box;margin:0;padding:0}
html,body{width:1200px;height:5102px;overflow:hidden;background:var(--white)}
body{position:relative;font-family:"Open Sans",sans-serif;color:var(--ink)}
.abs{position:absolute}
.photo{position:absolute;overflow:hidden}
.btn{position:absolute;display:flex;align-items:center;justify-content:center;border-radius:22px;font-family:"Libre Baskerville",serif;font-weight:700;font-size:14px;letter-spacing:.5px;text-transform:uppercase;white-space:nowrap}
.btn-green{background:var(--green);color:var(--white)}
.btn-gold{background:var(--gold);color:var(--white)}
.btn-outline{border:1.5px solid var(--green);color:var(--green);background:var(--white);font-size:10px;border-radius:14px}

/* header */
.site-header{position:absolute;left:0;top:0;width:1200px;height:114px;background:var(--white)}
.header-phone{position:absolute;left:150px;top:20px;display:flex;align-items:center;gap:12px;color:var(--gold);font-weight:600;font-size:17px}
.header-phone .icon{width:32px;height:32px;border-radius:50%;background:var(--green);display:flex;align-items:center;justify-content:center}
.nav{position:absolute;display:flex;justify-content:space-between;font-family:"Libre Baskerville",serif;font-size:11px;color:var(--ink);white-space:nowrap}
.nav .active{color:var(--gold)}
.brand{position:absolute;text-align:center;color:var(--green);font-family:"Libre Baskerville",serif}
.brand .mark{width:50px;height:50px;border-radius:50%;border:2px solid var(--gold);margin:0 auto 6px}
.brand .name{font-size:24px;letter-spacing:1px;line-height:1}
.brand .sub{font-size:9px;letter-spacing:6px;margin-top:4px}

/* hero */
.hero-circle{position:absolute;left:148px;top:180px;width:450px;height:450px;border-radius:50%;background:var(--green);border:8px solid var(--gold);display:flex;flex-direction:column;align-items:center;justify-content:center;text-align:center}
.hero-circle h1{font-family:"Libre Baskerville",serif;font-weight:400;color:var(--white);font-size:40px;line-height:54px;letter-spacing:1px}

/* sections */
.section-title{position:absolute;font-family:"Cinzel",serif;font-weight:700;font-size:52px;color:var(--green);letter-spacing:1px;line-height:1}
.section-title .accent{color:var(--gold)}
.copy{position:absolute;font-size:11.5px;line-height:16.5px;color:#333}

.service-card{position:absolute;width:286px;background:var(--white);box-shadow:0 4px 10px rgba(0,0,0,.12);text-align:center}
.service-card .thumb{height:190px}
.service-card h3{font-family:"Libre Baskerville",serif;font-weight:400;font-size:17px;color:var(--gold);margin-top:22px;line-height:22px;letter-spacing:.5px}
.service-card .btn{left:93px;width:100px;height:28px}
.service-card.featured{background:var(--gold)}
.service-card.featured h3{color:var(--white)}
.service-card.featured .btn{background:var(--green);color:var(--white);border-color:var(--green)}

.blog-card{position:absolute;width:252px;height:205px;background:var(--white);box-shadow:0 4px 12px rgba(0,0,0,.14);padding:18px 20px}
.blog-card .date{display:flex;align-items:center;gap:10px;font-size:13px;margin-bottom:12px}
.blog-card h4{font-size:11.5px;font-weight:600;line-height:16px;margin-bottom:8px}
.blog-card p{font-size:10px;line-height:13.5px;color:#444;margin-bottom:12px}
.blog-card .more{font-family:"Libre Baskerville",serif;font-size:12px;color:var(--gold)}

.field{position:absolute;border:1.5px solid rgba(255,255,255,.85);color:var(--white);font-size:11px;padding:8px 10px}

.site-footer{position:absolute;left:0;top:4650px;width:1200px;height:452px;background:var(--green)}
.footer-info{position:absolute;display:flex;gap:14px;color:var(--white)}
.footer-info .icon{width:34px;height:34px;border-radius:50%;background:var(--gold);display:flex;align-items:center;justify-content:center;flex:none}
.footer-info h5{font-family:"Libre Baskerville",serif;font-weight:400;font-size:18px;margin-bottom:8px}
.footer-info p{font-size:12px;line-height:15px}
.footer-legal{position:absolute;left:150px;top:344px;width:900px;text-align:center;font-size:10.5px;line-height:15px;color:rgba(255,255,255,.8)}
.social{position:absolute;width:30px;height:30px;border-radius:50%;background:var(--gold)}
</style>
</head>
<body>

<header class="site-header">
  <div class="header-phone">
    <span class="icon"><svg width="16" height="16" viewBox="0 0 24 24"><path fill="#fff" d="M6.6 10.8a15.1 15.1 0 0 0 6.6 6.6l2.2-2.2c.3-.3.7-.4 1-.2 1.1.4 2.3.6 3.6.6.6 0 1 .4 1 1V20c0 .6-.4 1-1 1C10.6 21 3 13.4 3 4c0-.6.4-1 1-1h3.5c.6 0 1 .4 1 1 0 1.3.2 2.5.6 3.6.1.3 0 .7-.2 1z"/></svg></span>
    555 014 2290
  </div>
  <nav class="nav" style="left:150px;top:76px;width:355px"><span class="active">Home</span><span>About Us</span><span>Services</span><span>Insights&amp;News</span><span>Careers</span></nav>
  <div class="brand" style="left:520px;top:8px;width:160px">
    <div class="mark"></div>
    <div class="name">BRANTLEY</div>
    <div class="sub">LAWYERS</div>
  </div>
  <nav class="nav" style="left:716px;top:76px;width:334px">
    <span>Costs</span><span>Contact Us</span><span>Compliance &amp; Disclaimers</span><span>Blog</span>
  </nav>
  <div class="btn btn-green" style="left:908px;top:14px;width:142px;height:44px">Live Chat</div>
</header>

<section class="hero">
  <div class="photo" role="img" aria-label="Lawyers reviewing documents together at a meeting table" style="left:0;top:114px;width:1200px;height:604px;background:linear-gradient(110deg,#3a3228 0%,#6b5c4a 30%,#2a3442 55%,#d9d6d0 80%,#b79d86 100%)"></div>
  <svg class="abs" style="left:0;top:560px" width="1200" height="160"><polygon points="585,160 710,10 880,160" fill="#fff"/></svg>
  <div class="hero-circle">
    <h1>ON YOUR SIDE<br>WHEN IT<br>MATTER MOST</h1>
    <div class="btn btn-gold" style="position:relative;margin-top:26px;width:176px;height:40px;font-size:13px">Get in Touch</div>
  </div>
</section>

<section class="about">
  <div class="photo" role="img" aria-label="Smiling lawyer in a suit pointing, framed by a circular emblem" style="left:150px;top:920px;width:412px;height:412px;border-radius:50%;background:radial-gradient(circle at 50% 45%,#2d2c2b 0%,#3a3835 50%,#7d6549 78%,#a88a62 100%)"></div>
  <h2 class="section-title" style="left:646px;top:908px">ABOUT <span class="accent">US</span></h2>
  <p class="copy" style="left:646px;top:990px;width:410px">Lorem ipsum dolor sit amet, consectetur adipiscing elit, sed do eiusmod tempor incididunt ut labore et dolore magna aliqua. Ut enim ad minim veniam, quis nostrud exercitation ullamco laboris nisi ut aliquip ex ea commodo consequat. Duis aute irure dolor in reprehenderit in voluptate velit esse cillum dolore eu fugiat nulla pariatur. Excepteur sint occaecat cupidatat non proident, sunt in culpa qui officia deserunt mollit anim id est laborum. Sed ut perspiciatis unde omnis iste natus error sit voluptatem accusantium doloremque laudantium, totam rem aperiam, eaque ipsa quae ab illo inventore veritatis et quasi architecto beatae vitae dicta sunt explicabo. Nemo enim ipsam voluptatem quia voluptas sit aspernatur aut odit aut fugit, sed quia consequuntur magni dolores eos qui ratione voluptatem sequi nesciunt. Neque porro quisquam est, qui dolorem ipsum quia dolor sit amet, consectetur, adipisci velit, sed quia non numquam eius modi tempora incidunt ut labore et dolore magnam aliquam quaerat voluptatem.</p>
  <div class="btn btn-green" style="left:646px;top:1240px;width:152px;height:42px">Read More</div>
</section>

<section class="services">
  <div class="abs" style="left:0;top:1428px;width:1200px;height:630px;background:var(--mist);clip-path:polygon(0 0,100% 0,100% 78%,0 100%)"></div>
  <h2 class="section-title" style="left:0;width:1200px;text-align:center;top:1488px">OUR SERVICES</h2>

  <article class="service-card featured" style="left:150px;top:1585px;height:295px">
    <div class="thumb" role="img" aria-label="Lawyer holding a stack of papers" style="background:linear-gradient(135deg,#b36b3c,#e7d3bd 60%,#3b2b24)"></div>
    <h3>ADMINISTARTIVE LAW</h3>
    <div class="btn btn-outline" style="top:242px">View All</div>
  </article>
  <article class="service-card" style="left:457px;top:1585px;height:295px">
    <div class="thumb" role="img" aria-label="Hands signing a contract" style="background:linear-gradient(135deg,#e6e1da,#8e7b6a 60%,#2d2a28)"></div>
    <h3>COMMERCIAL LAW</h3>
    <div class="btn btn-outline" style="top:242px">View All</div>
  </article>
  <article class="service-card" style="left:764px;top:1585px;height:295px">
    <div class="thumb" role="img" aria-label="Small house model beside property documents" style="background:linear-gradient(135deg,#4a4340,#b89a72 55%,#e9e5df)"></div>
    <h3>PROPERTY LAW</h3>
    <div class="btn btn-outline" style="top:242px">View All</div>
  </article>

  <article class="service-card" style="left:156px;top:1905px;height:310px">
    <div class="thumb" role="img" aria-label="Stamp on an immigration document" style="background:linear-gradient(135deg,#5c5650,#d8d2c8 55%,#8b7d6d)"></div>
    <h3>IMMIGRATION LAW</h3>
    <div class="btn btn-outline" style="top:256px">View All</div>
  </article>
  <article class="service-card" style="left:457px;top:1905px;height:310px">
    <div class="thumb" role="img" aria-label="Business people reviewing an employment contract" style="background:linear-gradient(135deg,#2c2c2e,#7b7672 50%,#d2ccc4)"></div>
    <h3>EMPLOYMENT LAW</h3>
    <div class="btn btn-outline" style="top:256px">View All</div>
  </article>
  <article class="service-card" style="left:764px;top:1905px;height:310px">
    <div class="thumb" role="img" aria-label="Family meeting with a lawyer" style="background:linear-gradient(135deg,#a08a78,#454a58 55%,#c9b8a6)"></div>
    <h3>FAMILY &amp;<br>RELATIONSHIP LAW</h3>
    <div class="btn btn-outline" style="top:256px">View All</div>
  </article>
</section>

<section class="join">
  <h2 class="section-title" style="left:150px;top:2418px">JOIN <span class="accent">US</span></h2>
  <p class="copy" style="left:150px;top:2512px;width:410px">Lorem ipsum dolor sit amet, consectetur adipiscing elit, sed do eiusmod tempor incididunt ut labore et dolore magna aliqua. Ut enim ad minim veniam, quis nostrud exercitation ullamco laboris nisi ut aliquip ex ea commodo consequat. Duis aute irure dolor in reprehenderit in voluptate velit esse cillum dolore eu fugiat nulla pariatur.</p>
  <div class="btn btn-green" style="left:150px;top:2618px;width:148px;height:44px">Join Now</div>
  <div class="photo" role="img" aria-label="Two professionals discussing documents in an office" style="left:632px;top:2318px;width:416px;height:416px;border-radius:50%;border:7px solid var(--gold);background:linear-gradient(135deg,#e9e6e1,#4b4e55 50%,#c6c1b9)"></div>
</section>

<section class="team">
  <div class="abs" style="left:0;top:2828px;width:1200px;height:590px;background:var(--green);clip-path:polygon(0 0,100% 0,100% 78%,0 100%)"></div>
  <h2 class="abs" style="left:0;width:1200px;text-align:center;top:2888px;font-family:'Libre Baskerville',serif;font-weight:700;font-size:46px;color:var(--white);letter-spacing:1px">MEET OUR TEAM</h2>
  <div class="photo" role="img" aria-label="Video of a judge and lawyers meeting in a courtroom office" style="left:186px;top:2995px;width:828px;height:470px;background:linear-gradient(100deg,#3b2a22 0%,#7a5a45 35%,#2b2320 55%,#8b6d58 75%,#d4c2b0 100%)"></div>
  <div class="abs" style="left:545px;top:3175px;width:110px;height:110px;border-radius:50%;background:#0d0d0d;display:flex;align-items:center;justify-content:center">
    <svg width="58" height="38" viewBox="0 0 58 38"><rect x="0" y="2" width="38" height="34" rx="6" fill="#fff"/><polygon points="40,19 58,6 58,32" fill="#fff"/></svg>
  </div>
</section>

<section class="blog">
  <h2 class="section-title" style="left:0;width:1200px;text-align:center;top:3580px">LATEST <span class="accent">BLOG</span></h2>

  <div class="photo" role="img" aria-label="Gavel and law books on a desk" style="left:150px;top:3683px;width:283px;height:172px;background:linear-gradient(135deg,#1e1b18,#7d5a36 55%,#2a2520)"></div>
  <article class="blog-card" style="left:166px;top:3843px">
    <div class="date"><svg width="22" height="22" viewBox="0 0 22 22"><rect x="1" y="3" width="20" height="18" rx="2" fill="var(--green)"/><rect x="5" y="0" width="3" height="5" fill="var(--green)"/><rect x="14" y="0" width="3" height="5" fill="var(--green)"/><rect x="4" y="9" width="14" height="9" fill="#fff" opacity=".85"/></svg>February 04,2023</div>
    <h4>Lorem ipsum dolor sit amet, conse ctetur magna dolor aliqua.</h4>
    <p>Lorem ipsum dolor sit amet, consectetur adipiscing elit, sed do eiusmod tempor incididunt ut labore et&nbsp; magna aliqua.</p>
    <div class="more">READ MORE</div>
  </article>

  <div class="photo" role="img" aria-label="Lawyer signing papers at a desk" style="left:458px;top:3683px;width:284px;height:172px;background:linear-gradient(135deg,#2a2624,#9a8a78 50%,#3a332d)"></div>
  <article class="blog-card" style="left:474px;top:3843px">
    <div class="date"><svg width="22" height="22" viewBox="0 0 22 22"><rect x="1" y="3" width="20" height="18" rx="2" fill="var(--green)"/><rect x="5" y="0" width="3" height="5" fill="var(--green)"/><rect x="14" y="0" width="3" height="5" fill="var(--green)"/><rect x="4" y="9" width="14" height="9" fill="#fff" opacity=".85"/></svg>February 04,2023</div>
    <h4>Lorem ipsum dolor sit amet, conse ctetur magna dolor aliqua.</h4>
    <p>Lorem ipsum dolor sit amet, consectetur adipiscing elit, sed do eiusmod tempor incididunt ut labore et&nbsp; magna aliqua.</p>
    <div class="more">READ MORE</div>
  </article>

  <div class="photo" role="img" aria-label="Scales of justice beside a lawyer at work" style="left:766px;top:3683px;width:284px;height:172px;background:linear-gradient(135deg,#3b3f44,#c7c3bb 50%,#8a7350)"></div>
  <article class="blog-card" style="left:782px;top:3843px">
    <div class="date"><svg width="22" height="22" viewBox="0 0 22 22"><rect x="1" y="3" width="20" height="18" rx="2" fill="var(--green)"/><rect x="5" y="0" width="3" height="5" fill="var(--green)"/><rect x="14" y="0" width="3" height="5" fill="var(--green)"/><rect x="4" y="9" width="14" height="9" fill="#fff" opacity=".85"/></svg>February 04,2023</div>
    <h4>Lorem ipsum dolor sit amet, conse ctetur magna dolor aliqua.</h4>
    <p>Lorem ipsum dolor sit amet, consectetur adipiscing elit, sed do eiusmod tempor incididunt ut labore et&nbsp; magna aliqua.</p>
    <div class="more">READ MORE</div>
  </article>
</section>

<section class="contact">
  <div class="abs" role="img" aria-label="Faint courtroom interior behind the contact form" style="left:0;top:4155px;width:1200px;height:495px;background:linear-gradient(180deg,#c49e52,#cda960 50%,#c6a258)"></div>
  <h2 class="abs" style="left:0;width:1200px;text-align:center;top:4222px;font-family:'Libre Baskerville',serif;font-weight:700;font-size:46px;color:var(--white);letter-spacing:1px">CONTACT US</h2>
  <div class="field" style="left:196px;top:4322px;width:256px;height:36px">Name</div>
  <div class="field" style="left:472px;top:4322px;width:256px;height:36px">Email Address</div>
  <div class="field" style="left:746px;top:4322px;width:256px;height:36px">Phone number</div>
  <div class="field" style="left:196px;top:4380px;width:806px;height:120px">Message</div>
  <div class="btn btn-green" style="left:540px;top:4530px;width:120px;height:42px">Submit</div>
</section>

<footer class="site-footer">
  <div class="brand" style="left:520px;top:48px;width:160px;color:var(--white)">
    <div class="mark" style="border-color:var(--white)"></div>
    <div class="name">BRANTLEY</div>
    <div class="sub">LAWYERS</div>
  </div>
  <nav class="nav" style="left:176px;top:200px;width:848px;color:var(--white)">
    <span>Home</span><span>About Us</span><span>Services</span><span>Insights&amp;News</span><span>Careers</span><span>Costs</span><span>Contact Us</span><span>Compliance &amp; Disclaimers</span><span>Blog</span>
  </nav>
  <div class="footer-info" style="left:234px;top:256px">
    <span class="icon"><svg width="16" height="18" viewBox="0 0 16 20"><path fill="#fff" d="M8 0a8 8 0 0 0-8 8c0 6 8 12 8 12s8-6 8-12a8 8 0 0 0-8-8zm0 11a3 3 0 1 1 0-6 3 3 0 0 1 0 6z"/></svg></span>
    <div><h5>Location</h5><p>123 ipsum dolor sit<br>amet, consectetur<br>adipiscing elit</p></div>
  </div>
  <div class="footer-info" style="left:534px;top:256px">
    <span class="icon"><svg width="16" height="16" viewBox="0 0 24 24"><path fill="#fff" d="M6.6 10.8a15.1 15.1 0 0 0 6.6 6.6l2.2-2.2c.3-.3.7-.4 1-.2 1.1.4 2.3.6 3.6.6.6 0 1 .4 1 1V20c0 .6-.4 1-1 1C10.6 21 3 13.4 3 4c0-.6.4-1 1-1h3.5c.6 0 1 .4 1 1 0 1.3.2 2.5.6 3.6.1.3 0 .7-.2 1z"/></svg></span>
    <div><h5>Call Us</h5><p>555 014 2290</p></div>
  </div>
  <div class="footer-info" style="left:810px;top:256px">
    <span class="icon"><svg width="16" height="12" viewBox="0 0 16 12"><rect width="16" height="12" rx="1" fill="#fff"/><path d="M0 1l8 6 8-6" stroke="var(--gold)" stroke-width="1.5" fill="none"/></svg></span>
    <div><h5>Email</h5><p>info@brantleylawyers.example</p></div>
  </div>
  <p class="footer-legal">Liability limited by a Scheme approved under Professional Standards Legislation. All legal practitioners employed by Brantley Lawyers Pty Limited (including those described as Principal Solicitor) are members of the Scheme.</p>
  <div class="abs" style="left:150px;top:388px;width:900px;height:1px;background:rgba(255,255,255,.25)"></div>
  <p class="abs" style="left:150px;top:414px;font-size:10px;color:var(--white);font-family:'Libre Baskerville',serif">COPYRIGHT © 2023 BRANTLEY LAWYERS. ALL RIGHTS RESERVED</p>
  <span class="social" style="left:934px;top:404px" aria-label="Social profile"></span>
  <span class="social" style="left:974px;top:404px" aria-label="Social profile"></span>
  <span class="social" style="left:1014px;top:404px" aria-label="Social profile"></span>
</footer>

</body>
</html>
```